Brivomark Business Card

Brivomark is a young and energetic software development consultancy. We spend our time on the road working with clients on their sites an meeting new potential customers and employees!

We need a sharp, vibrant and memorable business card that will inspires those that receive it to look after it as it oozes quality and is a nice thing in its own right.

We like bold colours and distinctive design. So show us what you can do.

In terms of information on the card, it would be good to see:

* Our logo (Obviously :) )
* Employee name
* Email
* Website address
* Mobile number
* Full company name (Brivomark ltd)
* Registered company number
* Registered company address

Industry/Entity Type

Software

Requirements
Nice to have
• We are thinking that having a QR Code on the business card could be a good way of adding active marketing. It would be good to see if you are able to merge the kind of element in to your designs!

Maybe something special could be achieved using a visual QR Code like those produced at http://www.quenprint-example.com/ ? You have our media so feel free to have a play.

```html
<!DOCTYPE html>
<html lang="en">
<head>
<meta charset="utf-8">
<title>Brivomark Business Card</title>
<link rel="stylesheet" href="https://fonts.googleapis.com/css2?family=Open+Sans:wght@400;600;700&display=swap">
<style>
  :root {
    --stage: #2e2621;
    --card-red: #cf1129;
    --card-red-deep: #b40d22;
    --card-red-press: #a90b1f;
    --card-white: #f2f1ee;
    --ink-grey: #4d4d4d;
    --ink-soft: #6b6b6b;
    --brand-red: #c8102e;
    --paper-white: #ffffff;
  }
  * { margin: 0; padding: 0; box-sizing: border-box; }
  html, body {
    width: 1200px;
    height: 900px;
    overflow: hidden;
    background: var(--stage);
    font-family: "Open Sans", Arial, sans-serif;
  }
  .canvas {
    width: 1200px;
    height: 900px;
    display: flex;
    align-items: center;
    justify-content: center;
    gap: 40px;
  }
  .card {
    width: 540px;
    height: 309px;
    border-radius: 3px;
    position: relative;
    box-shadow: 0 10px 30px rgba(0,0,0,0.45);
    overflow: hidden;
  }

  /* Front: red face */
  .card-front {
    background: linear-gradient(160deg, var(--card-red) 0%, var(--card-red-deep) 100%);
  }
  .card-front .brand-name {
    position: absolute;
    left: 0; right: 0;
    top: 100px;
    text-align: center;
    font-weight: 600;
    font-size: 62px;
    letter-spacing: 1px;
    color: var(--card-red-press);
  }
  .card-front .website {
    position: absolute;
    left: 0; right: 0;
    bottom: 38px;
    text-align: center;
    font-weight: 600;
    font-size: 17px;
    letter-spacing: 3px;
    color: var(--paper-white);
  }

  /* Back: white face */
  .card-back {
    background: var(--card-white);
  }
  .card-back .brand-name {
    position: absolute;
    left: 0; right: 0;
    top: 60px;
    text-align: center;
    font-weight: 600;
    font-size: 44px;
    letter-spacing: 0.5px;
    color: var(--brand-red);
  }
  .card-back .holder-name {
    position: absolute;
    left: 0; right: 0;
    top: 138px;
    text-align: center;
    font-weight: 700;
    font-size: 18px;
    color: var(--ink-grey);
  }
  .contact {
    position: absolute;
    left: 28px;
    right: 28px;
    bottom: 30px;
    font-size: 11.5px;
    line-height: 1.9;
    color: var(--ink-soft);
  }
  .contact-row { display: flex; gap: 18px; white-space: nowrap; }
  .contact .label {
    color: var(--brand-red);
    font-weight: 600;
    margin-right: 5px;
  }
</style>
</head>
<body>
<main class="canvas">
  <section class="card card-front" aria-label="Card front">
    <div class="brand-name">Brivomark</div>
    <div class="website">www.brivomark.com</div>
  </section>

  <section class="card card-back" aria-label="Card back">
    <div class="brand-name">Brivomark</div>
    <div class="holder-name">Daniel Harper</div>
    <div class="contact">
      <div class="contact-row">
        <span><span class="label">Brivomark ltd</span>101 Harlow Street, London</span>
        <span><span class="label">Reg.</span>01234567</span>
      </div>
      <div class="contact-row">
        <span><span class="label">Phone</span>020 7946 0318</span>
        <span><span class="label">Email</span>dan@brivomark.com</span>
      </div>
    </div>
  </section>
</main>
</body>
</html>
```